Regional Consulting Business Needs a Business Card Design

We need a business card design for our new business based in Regional Victoria, Australia called Larkwell Energy. We are a consulting company with our main goal being to save people momey money and reducing their carbon footprint. Anything from water saving showerheads, to energy saving lightglobes and even to solar power. We would like to see designs that use bright colours. The final design should shout 'we are here to help you'.

Industry/Entity Type

Business

```html
<!DOCTYPE html>
<html lang="en">
<head>
<meta charset="utf-8">
<title>Larkwell Energy – Business Card</title>
<link href="https://fonts.googleapis.com/css2?family=Arimo:wght@400;700&display=swap" rel="stylesheet">
<style>
  :root {
    --backdrop: #3c3c3c;
    --silver-light: #ffffff;
    --silver-mid: #e4e4e4;
    --silver-dark: #cfcfcf;
    --ink: #3f3f41;
    --ink-soft: #555557;
    --accent: #f2a516;
    --accent-deep: #e38b0c;
    --rule: #8a8a8a;
  }
  * { margin: 0; padding: 0; box-sizing: border-box; }
  html, body { width: 1200px; height: 900px; overflow: hidden; }
  body {
    background: var(--backdrop);
    font-family: "Arimo", Arial, sans-serif;
    color: var(--ink);
    position: relative;
  }
  .card {
    position: absolute;
    top: 300px;
    width: 525px;
    height: 300px;
    border-radius: 22px;
    overflow: hidden;
    background: linear-gradient(160deg, var(--silver-dark) 0%, var(--silver-light) 35%, var(--silver-mid) 55%, var(--silver-light) 75%, var(--silver-dark) 100%);
  }
  .card--front { left: 58px; }
  .card--back { left: 617px; }

  /* Front */
  .front-mark {
    position: absolute;
    left: 232px; top: 358px;
    width: 62px; height: 62px;
    background: linear-gradient(135deg, var(--accent), var(--accent-deep));
  }
  .brand-name {
    font-weight: 700;
    color: var(--ink);
    letter-spacing: -0.5px;
    white-space: nowrap;
  }
  .front .brand-name, .card--front .brand-name {
    position: absolute; left: 0; right: 0; top: 200px;
    text-align: center; font-size: 42px;
  }
  .tagline {
    font-weight: 700;
    color: var(--ink-soft);
    white-space: nowrap;
  }
  .card--front .tagline {
    position: absolute; left: 0; right: 0; top: 247px;
    text-align: center; font-size: 12px;
  }
  .card--front .front-mark { left: 232px; top: 58px; position: absolute; }

  /* Back */
  .back-header {
    position: absolute; left: 0; top: 0;
    width: 100%; height: 148px;
    background: var(--silver-light);
  }
  .back-notch {
    position: absolute; left: 76px; top: 148px;
    width: 0; height: 0;
    border-left: 12px solid transparent;
    border-right: 12px solid transparent;
    border-top: 12px solid var(--ink);
  }
  .back-mark {
    position: absolute; left: 40px; top: 48px;
    width: 48px; height: 48px;
    background: linear-gradient(135deg, var(--accent), var(--accent-deep));
  }
  .card--back .brand-name {
    position: absolute; left: 148px; top: 58px; font-size: 33px;
  }
  .card--back .tagline {
    position: absolute; left: 188px; top: 95px; font-size: 10px;
  }
  .contact { position: absolute; font-size: 13px; line-height: 16px; color: var(--ink); }
  .contact .label { color: var(--accent); }
  .person { left: 48px; top: 180px; }
  .person-name { font-size: 17px; margin-bottom: 12px; }
  .person-role { font-size: 12px; margin-left: 4px; }
  .website { font-size: 15px; margin-top: 10px; }
  .divider {
    position: absolute; left: 311px; top: 183px;
    width: 1px; height: 88px; background: var(--rule);
  }
  .office { left: 330px; top: 180px; font-size: 12.5px; line-height: 15.5px; }
  .office .phones { margin-top: 16px; }
</style>
</head>
<body>
  <section class="card card--front" aria-label="Business card front">
    <div class="front-mark"></div>
    <h1 class="brand-name">Larkwell Energy</h1>
    <p class="tagline">Maintanence and consulting services</p>
  </section>

  <section class="card card--back" aria-label="Business card back">
    <div class="back-header"></div>
    <div class="back-notch"></div>
    <div class="back-mark"></div>
    <h2 class="brand-name">Larkwell Energy</h2>
    <p class="tagline">Maintanence and consulting services</p>

    <div class="contact person">
      <p class="person-name">John Doe<span class="person-role">Manager</span></p>
      <p><span class="label">Mobile:</span> 000 000 000</p>
      <p><span class="label">Email:</span> johndoe@larkwellenergy.com</p>
      <p class="website">www.LarkwellEnergy.com</p>
    </div>

    <div class="divider"></div>

    <div class="contact office">
      <p>00 Your Street</p>
      <p>000000 000 000 0000</p>
      <p>PO Box 000</p>
      <div class="phones">
        <p><span class="label">Ph:</span> +00 7 0000 0000</p>
        <p><span class="label">Fax:</span> + 00 7 0000 0000</p>
      </div>
    </div>
  </section>
</body>
</html>
```